Darrow Consulting needs a quality & professional business card!

I am a recruitment and employment consultant from Brisbane, Australia and I had a fantastic logo organised by this community to I am hoping the business card will be the same.

I have attached the Darrow consulting logo that ideally would feature on the back of the business card. There are a number of logos for you to use as you see fit. I would like the colour cheme to match that of the Darrow Consulting logo. I also have a secondary company called Career Lantern Australia and I have included that logo as well. While it is an important part of the business I don't want this logo feature too predominantly as I am moving out of this space. This logo was created by myself and is of low quality. Feel free to use the icon and words however you want. The winning design will be smart, professional and eye-catching.

The information I am looking for in the business card is:
Name: Gavin Darrow
Position: Founder & Director
Phone: (07) 3519 6482
Mobile: 0431 586 207
Email: gavin@careerlantern.com.au

Target Market(s)

Recruiters, government, large companies

Contact Information for Business Card

Name: Gavin Darrow
Phone: (07) 3519 6482
Mobile: 0431 586 207
Web: www.careerlantern.com.au

Font styles to use
Serif
Sans Serif

Requirements
Must have
• Darrow Consulting Logo on reverse side
• Contact details on front side with smaller reference to Darrow Consulting logo and Career Lantern Australia logo

```html
<!DOCTYPE html>
<html lang="en">
<head>
<meta charset="utf-8">
<title>Darrow Consulting – Business Card</title>
<link rel="stylesheet" href="https://fonts.googleapis.com/css2?family=Merriweather:wght@400;700&family=Open+Sans:wght@400;600&family=Montserrat:wght@400;500&display=swap">
<style>
  :root {
    --page: #ecebe8;
    --card-white: #f7f7f7;
    --charcoal: #202326;
    --charcoal-light: #45484c;
    --accent-blue: #1e88c0;
    --back-blue: #0b8ec9;
    --ink-dark: #2a2c2f;
    --ink-grey: #55585c;
    --white: #ffffff;
  }
  html, body {
    margin: 0;
    width: 1200px;
    height: 950px;
    overflow: hidden;
    background: var(--page);
  }
  .canvas {
    position: relative;
    width: 1200px;
    height: 950px;
  }
  .card {
    position: absolute;
    top: 320px;
    width: 540px;
    height: 310px;
    box-shadow: 0 6px 18px rgba(0,0,0,0.18);
  }
  .card--front { left: 40px; }
  .card--back  { left: 620px; }
  .card svg { display: block; }

  .brand-name   { font-family: 'Merriweather', serif; font-weight: 700; font-size: 30px; fill: var(--ink-dark); }
  .brand-region { font-family: 'Open Sans', sans-serif; font-weight: 400; font-size: 16px; fill: var(--ink-grey); }
  .person-name  { font-family: 'Merriweather', serif; font-weight: 400; font-size: 22px; fill: var(--accent-blue); }
  .person-role  { font-family: 'Merriweather', serif; font-weight: 700; font-size: 16px; fill: var(--white); }
  .contact-line { font-family: 'Merriweather', serif; font-weight: 400; font-size: 10.5px; fill: var(--white); }
  .web-line     { font-family: 'Merriweather', serif; font-weight: 400; font-size: 11px; letter-spacing: 3px; fill: var(--white); }

  .back-name    { font-family: 'Montserrat', sans-serif; font-weight: 500; font-size: 40px; letter-spacing: 4px; fill: var(--white); }
  .back-sub     { font-family: 'Montserrat', sans-serif; font-weight: 500; font-size: 15px; letter-spacing: 9px; fill: var(--white); }
  .back-web     { font-family: 'Montserrat', sans-serif; font-weight: 400; font-size: 11px; letter-spacing: 5px; fill: var(--white); }
</style>
</head>
<body>
<main class="canvas">

  <section class="card card--front" aria-label="Front of business card">
    <svg width="540" height="310" viewBox="0 0 540 310">
      <defs>
        <linearGradient id="charcoal-sheen" x1="0" y1="1" x2="1" y2="0">
          <stop offset="0" stop-color="var(--charcoal-light)"/>
          <stop offset="0.6" stop-color="var(--charcoal)"/>
          <stop offset="1" stop-color="var(--charcoal)"/>
        </linearGradient>
      </defs>
      <rect class="card-base" width="540" height="310" fill="var(--card-white)"/>
      <path class="accent-curve" d="M540 50 Q 322 190 0 276" fill="none" stroke="var(--accent-blue)" stroke-width="3.5"/>
      <path class="dark-panel" d="M540 60 Q 330 200 0 285 L0 310 L540 310 Z" fill="url(#charcoal-sheen)"/>

      <g class="brand">
        <circle cx="62" cy="118" r="20" fill="var(--ink-grey)"/>
        <text class="brand-name" x="92" y="122">Career Lantern</text>
        <text class="brand-region" x="94" y="146">Australia</text>
      </g>

      <g class="contact" text-anchor="end">
        <text class="person-name" x="520" y="196">Gavin Darrow</text>
        <text class="person-role" x="520" y="224">Founder &amp; Director</text>
        <text class="contact-line" x="520" y="260">P.(07) 3519 6482 M.0431 586 207 E.gavin@careerlantern.com.au</text>
        <text class="web-line" x="520" y="286">www.careerlantern.com.au</text>
      </g>
    </svg>
  </section>

  <section class="card card--back" aria-label="Back of business card">
    <svg width="540" height="310" viewBox="0 0 540 310">
      <rect class="card-base" width="540" height="310" fill="var(--back-blue)"/>
      <g class="brand" text-anchor="middle">
        <text class="back-name" x="270" y="158">DARROW</text>
        <text class="back-sub" x="274" y="186">CONSULTING</text>
      </g>
      <text class="back-web" x="270" y="282" text-anchor="middle">www.careerlantern.com.au</text>
    </svg>
  </section>

</main>
</body>
</html>
```